Business Cards for IT Consulting Company (Managed Service Provider)

I am looking to have some business cards printed and would like some designs. We are an IT Consulting company based in Vancouver BC. I would like a nice clean and modern look to the cards. I have uploaded all the versions of my logo so parts can be used as needed. Here is a snippit from our website homepage:

Kelbrook Systems Ltd. is an IT Solutions Partner located in Vancouver BC, Canada. We offer IT solutions and support to customers in the greater Vancouver Area. With expertise in Microsoft platforms, as well as Linux and Mac OSX and over 12 years experience in the IT industry, Kelbrook Systems is dedicated to offering our clients top quality service and products. We take pride in the solutions we offer our customers. The greatest compliment a client can give us is to recommend our services.

Kelbrook Systems Ltd. offers a wide range of IT services from onsite service to remote support and managed service solutions. This allows clients to choose the support path that best suits their company’s needs. Supporting many different sized companies from small to enterprise level over the past 12 years Kelbrook Systems has the experience and expertise needed to ensure things run smoothly. Allowing our clients to focus on doing business.

Revolutionizing the way IT services are delivered.

Kelbrook Systems is dedicated to providing our clients with IT solutions that work and grow with them for years to come. This philosophy helps save money in the long run instead of replacing equipment constantly. Far too often IT solutions are not well thought out and while possibly solving the problem at hand, require replacement due to growth or quality within a very short time frame. Kelbrook Systems takes pride in providing solutions that will last and be able to accommodate growth without the need for replacement.

Industry/Entity Type

Information Technology

Contact Information for Business Card

Kelbrook Systems Ltd.
(Employee Name)
Eml: (Employees Email Address)
Web: kelbrook.me
Ph: 604-555-0142

Font styles to use
Serif
Sans Serif

Requirements
Must have
• The Company logo and company colors.
Nice to have
• - Our tag line: "Revolutionizing IT Services" or "Revolutionizing the way IT services are delivered."
• - Also I really like the idea of nature and technology together blending which is sort of where my logo came from so integrating that somehow onto the business cards would be great.

```html
<!DOCTYPE html>
<html lang="en">
<head>
<meta charset="utf-8">
<title>Kelbrook Systems Ltd. — Business Cards</title>
<link rel="stylesheet" href="https://fonts.googleapis.com/css2?family=Montserrat:wght@400;500;600&display=swap">
<style>
  :root {
    --bg: #d4d4d4;
    --charcoal: #5a5a5a;
    --brand-blue: #0a8fd6;
    --brand-blue-soft: #cfe7f6;
    --paper: #f4f4f4;
    --ink-grey: #555555;
    --white: #ffffff;
  }
  * { box-sizing: border-box; margin: 0; padding: 0; }
  html, body {
    width: 1200px; height: 800px; overflow: hidden;
    background: var(--bg);
    font-family: "Montserrat", Arial, sans-serif;
  }
  .stage {
    width: 1200px; height: 800px;
    display: flex; align-items: center; justify-content: center; gap: 60px;
  }
  .card {
    position: relative;
    width: 525px; height: 300px;
    overflow: hidden;
    box-shadow: 0 6px 18px rgba(0,0,0,0.12);
  }
  /* Front */
  .card-front { background: var(--charcoal); color: var(--white); }
  .card-front .decor {
    position: absolute; top: 0; right: 0;
    width: 245px; height: 100%;
    clip-path: polygon(32% 0, 100% 0, 100% 100%, 0 100%, 0 62%);
    background:
      radial-gradient(circle at 62% 48%, var(--brand-blue-soft) 0%, rgba(207,231,246,0.55) 38%, rgba(244,244,244,0) 72%),
      var(--paper);
  }
  .brand {
    display: flex; align-items: center; gap: 10px;
    color: var(--brand-blue);
    font-weight: 600;
    white-space: nowrap;
  }
  .brand-mark { display: block; background: var(--brand-blue); flex: none; }
  .card-front .brand {
    position: absolute; left: 38px; top: 60px;
    font-size: 19px; letter-spacing: 0.2px;
  }
  .card-front .brand-mark { width: 13px; height: 13px; }
  .person { position: absolute; left: 38px; top: 170px; }
  .person-name {
    color: var(--brand-blue); font-weight: 600;
    font-size: 15px; letter-spacing: 0.6px; text-transform: uppercase;
  }
  .person-role { font-size: 12.5px; margin-top: 3px; color: var(--white); }
  .contact-list { list-style: none; margin-top: 12px; }
  .contact-list li {
    display: flex; align-items: center; gap: 9px;
    font-size: 13px; line-height: 21px; color: var(--white);
  }
  .contact-icon {
    width: 15px; height: 15px; border-radius: 2px;
    background: var(--brand-blue);
    display: flex; align-items: center; justify-content: center;
  }
  .contact-icon svg { width: 11px; height: 11px; }
  /* Back */
  .card-back {
    background: var(--paper);
    display: flex; flex-direction: column; align-items: center; justify-content: center;
  }
  .card-back .brand { font-size: 30px; }
  .card-back .brand-mark { width: 22px; height: 22px; }
  .web-line {
    margin-top: 40px; font-size: 13px; color: var(--ink-grey); letter-spacing: 0.3px;
  }
</style>
</head>
<body>
<main class="stage">
  <section class="card card-front" aria-label="Business card front">
    <div class="decor" role="img" aria-label="Large outlined brand emblem decoration in blue on a white panel"></div>
    <div class="brand">
      <span class="brand-mark" aria-hidden="true"></span>
      <span class="brand-name">Kelbrook Systems Ltd.</span>
    </div>
    <div class="person">
      <p class="person-name">Jordan Mercer</p>
      <p class="person-role">General Manager</p>
      <ul class="contact-list">
        <li>
          <span class="contact-icon" aria-hidden="true">
            <svg viewBox="0 0 12 12"><path d="M3 1.5 L4.6 3.6 L3.7 4.8 Q4.8 7 7.2 8.3 L8.4 7.4 L10.5 9 L9.4 10.6 Q4.5 10 1.5 3 Z" fill="#fff"/></svg>
          </span>604-555-0142
        </li>
        <li>
          <span class="contact-icon" aria-hidden="true">
            <svg viewBox="0 0 12 12"><rect x="1.5" y="3" width="9" height="6" fill="none" stroke="#fff" stroke-width="1.1"/><path d="M1.5 3 L6 6.5 L10.5 3" fill="none" stroke="#fff" stroke-width="1.1"/></svg>
          </span>info@kelbrook.me
        </li>
        <li>
          <span class="contact-icon" aria-hidden="true">
            <svg viewBox="0 0 12 12"><circle cx="6" cy="6" r="4.3" fill="none" stroke="#fff" stroke-width="1"/><ellipse cx="6" cy="6" rx="1.8" ry="4.3" fill="none" stroke="#fff" stroke-width="0.9"/><path d="M1.7 6 H10.3" stroke="#fff" stroke-width="0.9"/></svg>
          </span>www.kelbrook.me
        </li>
      </ul>
    </div>
  </section>

  <section class="card card-back" aria-label="Business card back">
    <div class="brand">
      <span class="brand-mark" aria-hidden="true"></span>
      <span class="brand-name">Kelbrook Systems Ltd.</span>
    </div>
    <p class="web-line">www.kelbrook.me</p>
  </section>
</main>
</body>
</html>
```